" Empresa privada voltada a prestação de serviços nos ramos do direito Administrativo, Previdenciário, Tributário e Municipal, para particulares e pessoas jurídicas de direito público. "

```html
<!DOCTYPE html>
<html lang="pt-BR">
<head>
<meta charset="UTF-8">
<title>Moreira &amp; Lins – Papel Timbrado</title>
<link href="https://fonts.googleapis.com/css2?family=Cormorant+Garamond:wght@400&family=Montserrat:wght@400&display=swap" rel="stylesheet">
<style>
  :root {
    --backdrop: #ececec;
    --paper: #ffffff;
    --ink: #5e5e5e;
    --ink-soft: #8a8a8a;
    --ink-faint: #f1f1f1;
    --tab: #6b6b6b;
    --rule: #9a9a9a;
  }
  * { margin: 0; padding: 0; box-sizing: border-box; }
  html, body {
    width: 1200px; height: 1200px; overflow: hidden;
    background: var(--backdrop);
  }
  .letterhead {
    position: absolute;
    left: 204px; top: 40px;
    width: 792px; height: 1120px;
    background: var(--paper);
    box-shadow: 0 2px 10px rgba(0,0,0,0.08);
  }
  .edge-tab {
    position: absolute; left: 0; top: 56px;
    width: 8px; height: 34px;
    background: var(--tab);
  }
  .brand {
    position: absolute; text-align: center;
    font-family: "Cormorant Garamond", serif;
    font-weight: 400; color: var(--ink);
  }
  .brand__mark {
    display: block; margin: 0 auto 8px;
    width: 22px; height: 22px;
    background: var(--ink);
  }
  .brand__name { letter-spacing: 0.08em; text-transform: uppercase; white-space: nowrap; }
  .brand__tagline {
    font-family: "Montserrat", sans-serif;
    text-transform: uppercase; color: var(--ink-soft);
    white-space: nowrap;
  }
  .brand--header { right: 60px; top: 58px; }
  .brand--header .brand__name { font-size: 30px; }
  .brand--header .brand__tagline { font-size: 8.5px; letter-spacing: 0.42em; margin-top: 4px; }
  .brand--footer { right: 60px; bottom: 42px; }
  .brand--footer .brand__mark { width: 12px; height: 12px; margin-bottom: 4px; }
  .brand--footer .brand__name { font-size: 16px; }
  .brand--footer .brand__tagline { font-size: 5px; letter-spacing: 0.4em; margin-top: 2px; }
  .backdrop-mark {
    position: absolute; left: 130px; top: 270px;
    width: 300px; height: 300px;
    background: var(--ink-faint);
  }
  .contact {
    position: absolute; left: 48px; bottom: 122px;
    font-family: "Montserrat", sans-serif;
    font-size: 8px; line-height: 1.6;
    color: var(--ink-soft); list-style: none;
  }
  .footer-rule {
    position: absolute; left: 48px; right: 48px; bottom: 108px;
    height: 1px; background: var(--rule);
  }
</style>
</head>
<body>
  <main class="letterhead">
    <span class="edge-tab"></span>

    <header class="brand brand--header">
      <span class="brand__mark"></span>
      <div class="brand__name">Moreira &amp; Lins</div>
      <div class="brand__tagline">Advogados Associados</div>
    </header>

    <div class="backdrop-mark" aria-hidden="true"></div>

    <ul class="contact">
      <li>Tel. +55 (81) 3000-0000</li>
      <li>Rua das Palmeiras, 120, Sala 4</li>
      <li>Boa Viagem, Recife – PE</li>
      <li>contato@moreiralins.adv.br</li>
    </ul>

    <div class="footer-rule"></div>

    <footer class="brand brand--footer">
      <span class="brand__mark"></span>
      <div class="brand__name">Moreira &amp; Lins</div>
      <div class="brand__tagline">Advogados Associados</div>
    </footer>
  </main>
</body>
</html>
```